Electrical Wholesaler Needs a New Website

Looking for a new website to be built for an electrical wholesaler based in Birmingham(England). Our logo is based on two Lions with a shield, so ideally the site should be deigned around that.

Looking for something that shows off our logo and incorporates what we are trying to do, preferably to have a colour scheme that is green and black if possible.

Reason: Still undecided on what I'm looking for

Reason: Need more time to decide

Target Market(s)

I'm looking for a professional website for my company that doesn't just look like amother WordPress template that I could build myself.

Industry/Entity Type

Electrical

Font styles to use
Sans Serif

Colors
9bcb3c
cadf82

Requirements
Must have
• Website with 4-5 pages, home page, about us, suppliers list, catalogue download and contact us. Search for UK electrical wholesalers to give you an idea of what I mean.

```html
<!DOCTYPE html>
<html lang="en">
<head>
<meta charset="utf-8">
<title>Kestrel Electrical Wholesalers</title>
<link href="https://fonts.googleapis.com/css2?family=Ubuntu:wght@300;400;500;700&display=swap" rel="stylesheet">
<style>
:root{
  --green:#6aa81f;
  --green-light:#9bcb3c;
  --green-pale:#cadf82;
  --green-dark:#2f6a1a;
  --ink:#1d4a2a;
  --text:#666;
  --line:#d9d9d9;
  --bg:#f1f1f1;
}
*{margin:0;padding:0;box-sizing:border-box}
html,body{width:872px;height:1200px;overflow:hidden}
body{background:var(--bg);font-family:"Ubuntu",sans-serif;color:var(--text);position:relative}
.page{position:absolute;left:80px;top:0;width:711px;height:957px;background:#fff;border-left:1px solid #e2e2e2;border-right:1px solid #e2e2e2}
.abs{position:absolute}
.brand{left:26px;top:40px;display:flex;align-items:center;gap:8px}
.brand-mark{width:22px;height:22px;background:var(--green)}
.brand-name{font-size:17px;font-weight:700;color:var(--green-dark);line-height:1.05}
.utility{right:16px;top:11px;font-size:9.5px;color:#777}
.utility span{margin:0 3px;color:#aaa}
.social{right:13px;top:54px;display:flex;gap:6px}
.social i{display:block;width:16px;height:16px;border-radius:2px}
.search{left:506px;top:78px;width:194px;height:21px;border:1px solid var(--line);font-size:9px;color:#999;padding:5px 8px;background:#fff}
.search b{position:absolute;right:0;top:0;width:21px;height:19px;border-left:1px solid var(--line)}
.nav{left:0;top:113px;width:711px;height:33px;background:linear-gradient(#8cc63f,#5fa01c);display:flex}
.nav a{color:#fff;text-decoration:none;font-size:11px;display:flex;align-items:center;justify-content:center;border-right:1px solid rgba(255,255,255,.3)}
.nav a:last-child{border-right:0}
.hero{left:0;top:146px;width:711px;height:254px;background:linear-gradient(#fff 60%,#eee);border-bottom:1px solid #e3e3e3}
.hero h1{position:absolute;left:42px;top:56px;font-size:23px;font-weight:700;color:var(--green);letter-spacing:-.4px}
.hero h2{position:absolute;left:42px;top:86px;font-size:14.4px;font-weight:400;color:var(--ink)}
.hero p{position:absolute;left:42px;top:112px;width:300px;font-size:9.6px;line-height:15px;color:#777;font-weight:300}
.btn{background:linear-gradient(#79b52e,#4e8e17);color:#fff;border-radius:2px;font-size:9.5px;display:flex;align-items:center;justify-content:center}
.hero .btn{position:absolute;left:42px;top:148px;width:76px;height:22px}
.dots{position:absolute;left:44px;top:182px;display:flex;gap:3px}
.dots i{width:9px;height:9px;border-radius:50%;background:#bbb}
.dots i:first-child{background:#666}
.hero-visual{position:absolute;left:390px;top:12px;width:264px;height:236px;background:radial-gradient(ellipse 48% 50% at 50% 50%,#e4e6e8 0,#eef0f1 55%,rgba(255,255,255,0) 100%)}
.welcome{left:22px;top:428px;width:480px}
.welcome h3{font-size:19px;font-weight:400;color:var(--ink)}
.welcome .lead{font-size:11.6px;color:#555;margin-top:6px;font-weight:300}
.welcome p{font-size:9.4px;line-height:15.5px;color:#777;font-weight:300;margin-top:3px}
.welcome p + p{margin-top:7px}
.latest{left:28px;top:620px;font-size:19px;color:var(--ink);font-weight:400}
.card{width:114px;height:132px;border:1px solid #ddd;border-radius:3px;background:linear-gradient(#fff 70%,#f0f0f0)}
.card .thumb{position:absolute;left:12px;top:6px;width:90px;height:72px}
.card h4{position:absolute;left:12px;top:82px;font-size:11px;font-weight:400;color:var(--green)}
.card p{position:absolute;left:12px;top:98px;font-size:8px;line-height:12.5px;color:#888}
.why{left:522px;top:418px;width:176px;height:207px;border:1px solid #ddd;border-radius:3px}
.why h5{position:absolute;left:12px;top:12px;font-size:12.5px;font-weight:400;color:var(--green-dark);line-height:17px}
.why h5 b{font-size:16px;font-weight:400;display:block}
.why .photo{position:absolute;left:11px;top:53px;width:155px;height:66px;background:linear-gradient(90deg,#9fc19a,#cfe0c8 60%,#b8b3a4)}
.why p{position:absolute;left:11px;top:126px;width:158px;font-size:8.6px;line-height:14px;color:#888}
.why .btn{position:absolute;left:11px;top:171px;width:62px;height:18px;font-size:7.5px}
.say{left:523px;top:632px;width:175px;height:292px;border:1px solid #ddd;border-radius:3px;overflow:hidden}
.say h5{height:33px;background:linear-gradient(#8cc63f,#5fa01c);color:#fff;font-size:14px;font-weight:400;padding:9px 14px}
.quote{padding:13px 10px 0 15px;font-size:8.2px;line-height:13.6px}
.quote em{color:#777;display:block}
.quote b{display:block;font-weight:400;color:#444;margin-top:5px;font-size:9px;padding-bottom:9px;border-bottom:1px solid #ddd;margin-right:5px}
.quote:last-child b{border-bottom:0}
.footer{left:0;top:957px;width:872px;height:243px;background:linear-gradient(#5c9a2b,#7fb452 45%,#4d8f22)}
.col{top:37px;color:#fff}
.col h6{font-size:13.5px;font-weight:400;margin-bottom:8px}
.col a{display:block;color:#f0f7e8;font-size:9.5px;line-height:18.2px;font-weight:300;text-decoration:none}
.divider{top:32px;width:1px;height:126px;background:rgba(255,255,255,.2)}
.email{left:606px;top:1010px;width:157px;height:20px;background:#fff;border:1px solid #ccc;font-size:9px;color:#888;padding:4px 8px}
.subscribe{left:692px;top:1037px;width:71px;height:20px;background:#1f5a1f;color:#fff;font-size:9.5px;display:flex;align-items:center;justify-content:center;border-radius:2px}
.bottom{left:0;top:1158px;width:872px;height:42px;background:#4a8a1f;color:#d6ebc4;font-size:9.2px;padding:13px 115px;font-weight:300}
</style>
</head>
<body>
<div class="page">
  <div class="abs brand"><span class="brand-mark"></span><span class="brand-name">Kestrel<br>Electrical<br>Wholesalers</span></div>
  <div class="abs utility">My Acccount<span>|</span>Sign In<span>|</span>My Account<span>|</span>Cart - 0 items</div>
  <div class="abs social" aria-label="Social links">
    <i style="background:#3b5b98"></i><i style="background:#4fb5e4"></i><i style="background:#1c6fa6"></i><i style="background:#f29022"></i>
  </div>
  <div class="abs search">Find your product<b>
    <svg width="19" height="19" viewBox="0 0 19 19"><circle cx="9" cy="8.5" r="4" fill="none" stroke="#777" stroke-width="1.6"/><line x1="12" y1="11.5" x2="15" y2="14.5" stroke="#777" stroke-width="1.8"/></svg></b></div>
  <nav class="abs nav">
    <a style="width:74px">HOME</a><a style="width:84px">ABOUT US</a><a style="width:86px">PRODUCTS</a><a style="width:76px">SERVICES</a><a style="width:106px">BEST SELLINGS</a><a style="width:104px">TESTIMONIALS</a><a style="width:76px">SUPPORT</a><a style="width:105px">CONTACT</a>
  </nav>
  <section class="abs hero">
    <h1>ELECTRICAL WATER HEATERS</h1>
    <h2>We are Experts in Testing &amp; Electrical Services</h2>
    <p>Phasellus felis dolor, scelerisque a, tempus eget, lobortis id, libero. Donec scelerisque leo ac risus. Praesent sit amet</p>
    <div class="btn">Read More</div>
    <div class="dots"><i></i><i></i><i></i><i></i></div>
    <div class="hero-visual" role="img" aria-label="Group of white electric water heater tanks"></div>
  </section>
  <section class="abs welcome">
    <h3>Welcome to Our Website Mainpage..</h3>
    <div class="lead">Phasellus felis dolor scelerisque tempus eget lobortis id, libero.</div>
    <p>Donec scelerisque leo ac risus. Praesent sit amet est. In dictum, dolor eu dictum porttitor, enim felis viverra mi, eget luctus massa purus quis odio. Etiam nulla massa, pharetra facilisis, volutpat in, imperdiet sit amet, sem. Aliquam nec erat at purus cursus interdum. Vestibulum ligula augue, bibendum accumsan</p>
    <p>Vivamus porttitor, g, purus nisi eleifend libero, a tempus libero lectus feugiat felis. Morbi diam mauris, viverra in, gravida eu, mattis in, ante. Morbi eget arcu. Morbi porta, libero id ullamcorper nonummy, nibh ligula pulvinar metus, eget consectetuer augue nisi quis lacus. Ut ac mi quis lacus mollis aliquam. Curabitur iaculis tempus eros. Curabitur vel mi sit amet magna malesuada ultrices. Ut nisi erat, fermentum vel, congue</p>
  </section>
  <h3 class="abs latest">Latest Products</h3>

  <div class="abs card" style="left:27px;top:653px"><div class="thumb" role="img" aria-label="Fan heater" style="background:radial-gradient(ellipse 45% 48% at 50% 50%,#d6d6d6 0,#ececec 55%,rgba(255,255,255,0) 100%)"></div><h4>Product Name</h4><p>Fusce ultricies orci ac<br>feugiat suscipit leo</p></div>
  <div class="abs card" style="left:148px;top:653px"><div class="thumb" role="img" aria-label="Trunking with sockets" style="background:radial-gradient(ellipse 50% 40% at 50% 50%,#dcdcdc 0,#efefef 55%,rgba(255,255,255,0) 100%)"></div><h4>Product Name</h4><p>Fusce ultricies orci ac<br>feugiat suscipit leo</p></div>
  <div class="abs card" style="left:269px;top:653px"><div class="thumb" role="img" aria-label="Coils of coloured cable" style="background:radial-gradient(ellipse 50% 45% at 50% 50%,rgba(255,255,255,0) 35%,#fff 80%),linear-gradient(100deg,#4a86d0,#d84a4a 35%,#d9c24a 55%,#5aa040 75%,#8a5a40)"></div><h4>Product Name</h4><p>Fusce ultricies orci ac<br>feugiat suscipit leo</p></div>
  <div class="abs card" style="left:390px;top:653px"><div class="thumb" role="img" aria-label="Metal conduit coupling" style="background:radial-gradient(ellipse 45% 35% at 50% 50%,#b8b8b8 0,#e2e2e2 55%,rgba(255,255,255,0) 100%)"></div><h4>Product Name</h4><p>Fusce ultricies orci ac<br>feugiat suscipit leo</p></div>
  <div class="abs card" style="left:27px;top:792px"><div class="thumb" role="img" aria-label="Black conduit gland fitting" style="background:radial-gradient(ellipse 45% 38% at 50% 50%,#3a3a3a 0,#8a8a8a 50%,rgba(255,255,255,0) 100%)"></div><h4>Product Name</h4><p>Fusce ultricies orci ac<br>feugiat suscipit leo</p></div>
  <div class="abs card" style="left:148px;top:792px"><div class="thumb" role="img" aria-label="Grey conduit connector" style="background:radial-gradient(ellipse 45% 30% at 50% 50%,#5a5a5a 0,#a0a0a0 50%,rgba(255,255,255,0) 100%)"></div><h4>Product Name</h4><p>Fusce ultricies orci ac<br>feugiat suscipit leo</p></div>
  <div class="abs card" style="left:269px;top:792px"><div class="thumb" role="img" aria-label="Floor outlet box" style="background:radial-gradient(ellipse 48% 42% at 50% 50%,#8a9098 0,#c6cacf 55%,rgba(255,255,255,0) 100%)"></div><h4>Product Name</h4><p>Fusce ultricies orci ac<br>feugiat suscipit leo</p></div>
  <div class="abs card" style="left:390px;top:792px"><div class="thumb" role="img" aria-label="Four-way junction box" style="background:radial-gradient(ellipse 38% 45% at 50% 50%,#a8a8a8 0,#d8d8d8 55%,rgba(255,255,255,0) 100%)"></div><h4>Product Name</h4><p>Fusce ultricies orci ac<br>feugiat suscipit leo</p></div>

  <aside class="abs why">
    <h5>Why Choose<b>Our Products</b></h5>
    <div class="photo" role="img" aria-label="Office workspace with glass partitions"></div>
    <p>Phasellus felis dolor, scelerisque a, tempus eget, lobortis id, libero. Donec scelerisque leo ac risus.</p>
    <div class="btn">CLICK HERE</div>
  </aside>
  <aside class="abs say">
    <h5>What Customers Say</h5>
    <div class="quote"><em>Phasellus felis dolor, scelerisque a, tempus eget, lobortis id, libero. Donec scelerisque leo ac risus Praesent</em><b>By Author Name</b></div>
    <div class="quote"><em>Donec scelerisque leo ac risus. Praesent sit amet est. In dictum, dolor eu dictum porttitor, enim felis viverra mi, eget luctus massa purus quis odio.</em><b>By Author Name</b></div>
    <div class="quote"><em>Phasellus felis dolor, scelerisque a, tempus eget, lobortis id, libero. Donec scelerisque leo ac risus Praesent</em><b>By Author Name</b></div>
  </aside>
</div>

<footer class="abs footer">
  <div class="abs col" style="left:118px"><h6>PRODUCTS</h6><a>Proin nulla arcu</a><a>Nonummy luctus</a><a>Dictum eget</a><a>Fermentum lorem</a><a>Nunc porta</a></div>
  <div class="abs divider" style="left:205px"></div>
  <div class="abs col" style="left:231px"><h6>ABOUT</h6><a>Proin nulla arcu</a><a>Nonummy luctus</a><a>Dictum eget</a><a>Fermentum lorem</a><a>Nunc porta</a></div>
  <div class="abs divider" style="left:315px"></div>
  <div class="abs col" style="left:342px"><h6>RESOURCES</h6><a>Proin nulla arcu</a><a>Nonummy luctus</a><a>Dictum eget</a><a>Fermentum lorem</a><a>Nunc porta</a></div>
  <div class="abs divider" style="left:435px"></div>
  <div class="abs col" style="left:467px"><h6>SUPPORT</h6><a>Proin nulla arcu</a><a>Nonummy luctus</a><a>Dictum eget</a><a>Fermentum lorem</a><a>Nunc porta</a></div>
  <div class="abs divider" style="left:580px"></div>
  <div class="abs col" style="left:604px"><h6>SIGN UP NEWSLETTERS</h6></div>
</footer>
<div class="abs email">Email address</div>
<div class="abs subscribe">SUBSCRIBE</div>
<div class="abs bottom">© 2013 Company Name.&nbsp; All right reserved.&nbsp; Term of Use</div>
</body>
</html>
```